Online-Marketing Material für Nähmaschinen
Es wurde alles gut umgesetzt und der Kontakt war sehr freundlich und zuverlässig. Danke.
Zielgruppe
Wir verkaufen Nähmaschinen, Stickmaschinen, Overlock und Nähzubehör über unseren Laden und Onlineshop www.Fadenwelt-Haendler.de
Unsere Zielgruppe sind zu 95% Frauen im Alter von 20 - 65 Jahren.
Aufgabenstellung
Wir möchten gerne einen Werbebanner (Bannergröße 2320x540 Pixel) zum Black Friday für unsere Startseite im Onlineshop und Angebotsbilder zu gewissen Maschinen. Bezüglich den Angebotsbilder. Hier sollte bitte eine Umrandung erstellt werden, die wir dann um die Bilder legen können im Photoshop. Der Banner sollte folgendes enthalten.
- WILDE STOFF TAGE (statt Black Friday)
- bis zu 40% sparen
- gültig von 21. - 28.11.2022
Ich habe auch noch unser Firmenlogo und Bilder von Maschinen mit angehängt, die eingebaut werden könnten.
Es ist auch ein alter WILDE STOFF TAGE Banner als Vorlage in welche Richtung es gehen könnte.
Allerdings sind wir an etwas neuem sehr offen.
Viele Grüße
Matthias Lenhart

```html
<!DOCTYPE html>
<html lang="de">
<head>
<meta charset="utf-8">
<title>Wilde Stoff Tage – Banner</title>
<link href="https://fonts.googleapis.com/css2?family=Open+Sans:wght@700;800&display=swap" rel="stylesheet">
<style>
  :root {
    --fabric-red: #b8293f;
    --fabric-deep: #8e1c2e;
    --plate-grey: #c9c6c6;
    --plate-light: #e4e2e2;
    --ink: #0a0a0a;
    --paper: #ffffff;
    --accent-red: #c4303f;
    --brand-ink: #262626;
    --tile-shadow: rgba(0,0,0,0.28);
  }
  html, body {
    margin: 0;
    padding: 0;
    width: 1200px;
    height: 279px;
    overflow: hidden;
    background: var(--paper);
  }
  .banner {
    position: relative;
    width: 1200px;
    height: 279px;
    overflow: hidden;
    font-family: "Open Sans", "Segoe UI", Arial, sans-serif;
  }
  .banner__photo {
    position: absolute;
    inset: 0;
    background:
      radial-gradient(ellipse 420px 150px at 380px 180px, rgba(220,215,215,0.55), transparent 70%),
      linear-gradient(180deg, var(--fabric-red) 0%, var(--fabric-deep) 38%, var(--fabric-red) 55%, var(--plate-grey) 72%, var(--plate-light) 100%);
  }
  .headline {
    position: absolute;
    right: 254px;
    top: -4px;
    margin: 0;
    font-size: 87px;
    font-weight: 700;
    line-height: 1.1;
    letter-spacing: -0.5px;
    color: var(--ink);
    white-space: nowrap;
  }
  .offer {
    position: absolute;
    right: 252px;
    top: 86px;
    margin: 0;
    font-size: 47px;
    font-weight: 700;
    line-height: 1.2;
    color: var(--paper);
    white-space: nowrap;
  }
  .validity {
    position: absolute;
    left: 0;
    top: 0;
    width: 1200px;
    height: 279px;
  }
  .validity__text {
    font-family: "Open Sans", "Segoe UI", Arial, sans-serif;
    font-weight: 700;
    font-size: 23px;
    fill: var(--paper);
    font-weight: 400;
  }
  .brand {
    position: absolute;
    left: 786px;
    top: 226px;
    display: flex;
    align-items: center;
    gap: 8px;
  }
  .brand__name {
    font-size: 17px;
    font-weight: 800;
    line-height: 1.05;
    color: var(--brand-ink);
    letter-spacing: 0.3px;
  }
  .brand__mark {
    width: 20px;
    height: 20px;
    background: var(--accent-red);
    align-self: flex-end;
    margin-bottom: 2px;
  }
  .products {
    position: absolute;
    left: 1010px;
    top: 11px;
    display: grid;
    grid-template-columns: 82px 82px;
    grid-template-rows: 79px 79px 79px;
    column-gap: 9px;
    row-gap: 10px;
  }
  .products__tile {
    background: var(--paper);
    box-shadow: 0 0 4px var(--tile-shadow);
    display: flex;
    align-items: center;
    justify-content: center;
  }
  .products__image {
    width: 72px;
    height: 66px;
    background: radial-gradient(ellipse at 50% 60%, #e9e9ea 0%, #f7f7f7 60%, #ffffff 100%);
  }
</style>
</head>
<body>
  <div class="banner">
    <div class="banner__photo" role="img" aria-label="Nahaufnahme eines Nähmaschinenfußes mit rotem Faden auf rotem Stoff"></div>

    <h1 class="headline">WILDE STOFF TAGE</h1>
    <p class="offer">bis zu 40% sparen</p>

    <svg class="validity" viewBox="0 0 1200 279" aria-label="gültig von 21. - 28.11.2022">
      <polygon points="649,199 995,155 998,185 652,231" fill="var(--ink)"/>
      <polygon points="995,140 1027,170 995,202" fill="var(--accent-red)"/>
      <text class="validity__text" x="664" y="222" transform="rotate(-7.3 664 222)">gültig von 21. - 28.11.2022</text>
    </svg>

    <div class="brand">
      <div class="brand__name">FADENWELT<br>HÄNDLER</div>
      <div class="brand__mark"></div>
    </div>

    <div class="products">
      <div class="products__tile"><div class="products__image" role="img" aria-label="Coverlock-Maschine"></div></div>
      <div class="products__tile"><div class="products__image" role="img" aria-label="Overlock-Maschine mit Display"></div></div>
      <div class="products__tile"><div class="products__image" role="img" aria-label="Stickmaschine mit Stickrahmen"></div></div>
      <div class="products__tile"><div class="products__image" role="img" aria-label="Overlock-Maschine mit blauen Details"></div></div>
      <div class="products__tile"><div class="products__image" role="img" aria-label="Computer-Nähmaschine"></div></div>
      <div class="products__tile"><div class="products__image" role="img" aria-label="Computer-Nähmaschine mit Display"></div></div>
    </div>
  </div>
</body>
</html>
```